Therapist website

I need a sqaure space web design for my therapy practice. I need a home page, a services page with 4 subpages, an about me, an insurnace page, a contact page, an EMDR page

```html
<!DOCTYPE html>
<html lang="en">
<head>
<meta charset="utf-8">
<title>Willow Creek Family Counseling</title>
<link href="https://fonts.googleapis.com/css2?family=Mulish:ital,wght@0,400;0,600;0,700;1,400&family=Raleway:wght@400;700&display=swap" rel="stylesheet">
<style>
  :root {
    --teal: #1e8b8d;
    --ink: #1f2324;
    --card: #e4eaea;
    --white: #ffffff;
    --hero-a: #a9c48a;
    --hero-b: #7f9e62;
    --sky-a: #9dbad6;
    --sky-b: #b7cfe3;
    --wheat-a: #d3b473;
    --wheat-b: #bf9a57;
  }
  * { box-sizing: border-box; margin: 0; padding: 0; }
  html, body { width: 1200px; height: 2965px; overflow: hidden; background: var(--white); }
  body { position: relative; font-family: "Mulish", sans-serif; color: var(--ink); }

  .site-header { position: absolute; left: 0; top: 0; width: 1200px; height: 164px; }
  .menu-toggle { position: absolute; left: 132px; top: 78px; width: 26px; height: 18px; }
  .menu-toggle span { display: block; height: 3px; background: var(--ink); margin-bottom: 4.5px; }
  .brand { position: absolute; left: 0; width: 1200px; top: 36px; text-align: center; color: var(--teal); font-weight: 700; }
  .brand-dot { width: 44px; height: 44px; border-radius: 50%; background: var(--teal); margin: 0 auto 8px; }
  .brand-name { font-size: 26px; letter-spacing: 2px; line-height: 28px; }
  .brand-sub { font-size: 10px; letter-spacing: 3px; line-height: 16px; }
  .header-tools { position: absolute; left: 962px; top: 76px; display: flex; align-items: center; height: 24px; }
  .social-box { width: 16px; height: 16px; border-radius: 3px; background: var(--teal); margin-right: 9px; }
  .tools-divider { width: 1px; height: 30px; background: var(--teal); margin: 0 14px 0 4px; }

  .hero { position: absolute; left: 0; top: 164px; width: 1200px; height: 558px;
    background: linear-gradient(180deg, var(--hero-a), var(--hero-b)); }

  .intro-text { position: absolute; left: 100px; top: 774px; width: 540px; font-size: 16px; line-height: 28.5px; }
  .btn { display: inline-block; background: var(--teal); color: var(--white); border-radius: 30px; text-align: center; text-decoration: none; }
  .btn-appointment { position: absolute; left: 743px; top: 835px; width: 317px; height: 54px; line-height: 54px; font-size: 16px; }

  .feature { position: absolute; top: 1080px; width: 292px; }
  .feature h2 { color: var(--teal); font-weight: 600; font-size: 23px; letter-spacing: .5px; margin-bottom: 10px; }
  .feature p { font-size: 15.5px; line-height: 28px; }
  .feature a { color: var(--teal); text-decoration: none; font-size: 15.5px; line-height: 28px; }

  .photo { position: absolute; }
  .photo-laptop { left: 416px; top: 1451px; width: 679px; height: 357px;
    background: linear-gradient(180deg, var(--sky-a), var(--sky-b)); }
  .photo-field { left: 101px; top: 2212px; width: 679px; height: 358px;
    background: linear-gradient(180deg, var(--wheat-a), var(--wheat-b)); }

  .card { position: absolute; width: 436px; height: 282px; background: var(--card); padding: 30px 34px; }
  .card h2 { color: var(--teal); font-weight: 700; font-size: 24px; letter-spacing: .5px; margin-bottom: 18px; }
  .card p { font-size: 15px; line-height: 28px; margin-bottom: 14px; }
  .btn-small { height: 34px; line-height: 34px; padding: 0 24px; font-size: 15px; }
  .card-therapist { left: 101px; top: 1488px; }
  .card-approach { left: 670px; top: 2250px; }

  .quote { position: absolute; left: 0; top: 1948px; width: 1200px; text-align: center; font-style: italic; font-size: 21px; line-height: 36px; }

  .cta { position: absolute; left: 0; top: 2680px; width: 1200px; text-align: center; font-family: "Raleway", sans-serif; font-size: 28px; line-height: 38px; }
  .btn-schedule { position: absolute; left: 531px; top: 2777px; width: 134px; height: 54px; line-height: 54px; font-weight: 700; font-size: 16px; font-family: "Raleway", sans-serif; }

  .site-footer { position: absolute; left: 0; top: 2886px; width: 1200px; text-align: center; font-size: 11px; font-weight: 600; }
</style>
</head>
<body>
  <header class="site-header">
    <div class="menu-toggle"><span></span><span></span><span></span></div>
    <div class="brand">
      <div class="brand-dot"></div>
      <div class="brand-name">WILLOW CREEK</div>
      <div class="brand-sub">FAMILY COUNSELING</div>
    </div>
    <div class="header-tools">
      <span class="social-box"></span><span class="social-box"></span><span class="social-box"></span>
      <span class="tools-divider"></span>
      <svg width="20" height="20" viewBox="0 0 20 20" aria-label="Search"><circle cx="8" cy="8" r="6" fill="none" stroke="#1e8b8d" stroke-width="2.5"/><line x1="12.5" y1="12.5" x2="18" y2="18" stroke="#1e8b8d" stroke-width="3" stroke-linecap="round"/></svg>
    </div>
  </header>

  <div class="hero" role="img" aria-label="Photo: smiling family of four outdoors"></div>

  <p class="intro-text">Sed ut perspiciatis unde omnis iste natus error sit voluptat accusantium doloremque laudantium, totam rem aperiam, eaque ipsa quae ab illo inventore veritatis et quasi architecto beatae vitae dicta sunt explicabo. Nemo enim ipsam voluptatem quia voluptas sit aspern aut odit aut fut, sed quia consequuntur magni dolores eos qui ratione voluptatem sequi nesciunt.</p>
  <a class="btn btn-appointment" href="#">Make an Appointment</a>

  <section class="feature" style="left:108px">
    <h2>SERVICES</h2>
    <p>Psychotherapy for Children, Adolescents, and Adults, Family and Marital Therapy, Attachment/Adoption Therapy,Pre-Adoption Training</p>
    <a href="#">See all Services &raquo;</a>
  </section>
  <section class="feature" style="left:455px">
    <h2>ABOUT US</h2>
    <p>Lorem ipsum dolor sit amet, consectetur adipiscing elit, sed do eiusmod tempor incididunt ut labore et dolore magna aliqua.</p>
    <a href="#">Read More &raquo;</a>
  </section>
  <section class="feature" style="left:792px">
    <h2>EMDR</h2>
    <p>EMDR (Eye Movement Desensitization and Reprocessing) is a psychotherapy treatment developed by Dr. Helen Marsh.</p>
    <a href="#">Read More &raquo;</a>
  </section>

  <div class="photo photo-laptop" role="img" aria-label="Photo: woman sitting on grass with a laptop"></div>
  <section class="card card-therapist">
    <h2>MAREN ELLISON, LMFT</h2>
    <p>Welcome to Willow Creek Family Counseling and thank you for visiting my website to learn more about whether I may be a good fit for your current life struggle.</p>
    <a class="btn btn-small" href="#">Read More</a>
  </section>

  <blockquote class="quote">Lorem ipsum dolor sit amet, consectetur adipiscing elit, sed do eiusmod<br>tempor incididunt ut labore et dolore magna aliqua<br>— Blandit Lectus</blockquote>

  <div class="photo photo-field" role="img" aria-label="Photo: two women walking through a wheat field"></div>
  <section class="card card-approach">
    <h2>GENERAL APPROACH</h2>
    <p>I believe that many struggles are rooted in relationships and therefore practice from modalities and models that are based in relationship such as family systems and psychodynamic</p>
    <a class="btn btn-small" href="#">Read More</a>
  </section>

  <p class="cta">Let's talk!<br>Your first consultation is free.</p>
  <a class="btn btn-schedule" href="#">SCHEDULE</a>

  <footer class="site-footer">Copyrights © 2018 . Allrights Reserved.</footer>
</body>
</html>
```